Redesign existing website to have updated look and content

have existing website but do not have the time to put page detail that I want into it. we are a residential, family owned and operated HVAC and plumbing company. we offer service, repair, replacement, maintenance, new installations. the owner has over 20 years experience. got into his own business bc of high pricing charged by old employer. we believe CUSTOMER SERVICE IS THE ONLY THING THAT MATTERS, we are an harlow's guide top trade award winner. we just recently were invited to sell on Brindlemart. we currently have the owner and 1 other tech and a helper in the field. we want to keep small so that service doesn't suffer

Target Market(s)

homeowners over 28 in the Bucks and Montgomery and Delawre Counties of PA

Industry/Entity Type

Hvac

Number of Pages Required

4 page

Font styles to use
Serif
Sans Serif
Decorative

Colors
0255a3
ec1f27

Requirements
Must have
• more content and information
• online scheduling thru V Cita
• information that is not related to HVAC that can be updated daily
Nice to have
• apps that customers will be drawn to website with
• information regarding our services and costs
• online scheduling
• better content!!!!
• links to vendors and outside information

```html
<!DOCTYPE html>
<html lang="en">
<head>
<meta charset="utf-8">
<title>KVR Service – Residential HVAC &amp; Plumbing</title>
<link href="https://fonts.googleapis.com/css2?family=Open+Sans:wght@400;600;700;800&display=swap" rel="stylesheet">
<style>
  :root {
    --blue: #0255a3;
    --navy: #1b3764;
    --navy-dark: #0f2446;
    --red: #ec1f27;
    --orange: #f39a1e;
    --gold: #f5c21a;
    --ink: #333b45;
    --muted: #6b7480;
    --line: #d8dde3;
    --page: #eef0f2;
    --white: #ffffff;
  }
  * { box-sizing: border-box; margin: 0; padding: 0; }
  html, body { width: 867px; height: 1200px; overflow: hidden; }
  body { font-family: "Open Sans", Arial, sans-serif; color: var(--ink); background: var(--page); }
  .site { position: relative; width: 867px; height: 1200px; background: linear-gradient(#f6f7f8, #e4e7ea); }

  /* Header */
  .site-header { position: absolute; left: 0; top: 0; width: 867px; height: 100px; background: var(--white); }
  .brand { position: absolute; left: 30px; top: 20px; display: flex; align-items: center; gap: 12px; }
  .brand-mark { width: 46px; height: 46px; border-radius: 50%; background: var(--blue); }
  .brand-name { font-size: 30px; font-weight: 800; color: var(--blue); line-height: 1; }
  .topbar { position: absolute; right: 0; top: 0; width: 400px; height: 24px; background: var(--blue); display: flex; align-items: center; padding-left: 70px; gap: 6px; color: var(--white); font-size: 10px; }
  .social-dot { width: 13px; height: 13px; border-radius: 50%; background: rgba(255,255,255,.85); }
  .topbar .email { margin-left: 22px; display: flex; align-items: center; gap: 5px; }
  .topbar .phone { position: absolute; right: 0; top: 0; height: 24px; width: 112px; background: var(--orange); display: flex; align-items: center; justify-content: center; gap: 5px; font-weight: 700; }
  .main-nav { position: absolute; left: 352px; top: 68px; display: flex; gap: 30px; font-size: 11px; font-weight: 700; color: var(--navy); }
  .main-nav a { color: inherit; text-decoration: none; }
  .main-nav a.active { border-bottom: 2px solid var(--red); padding-bottom: 3px; }
  .buy-button { position: absolute; left: 738px; top: 60px; width: 110px; height: 26px; background: var(--gold); border-radius: 4px; font-size: 10px; font-weight: 700; color: var(--navy-dark); display: flex; align-items: center; justify-content: center; }

  /* Hero */
  .hero { position: absolute; left: 0; top: 100px; width: 867px; height: 320px; background: linear-gradient(180deg, #7f8a8e 0%, #c9cfcf 45%, #e6e3dc 75%, #b8b2a6 100%); }
  .hero-title { position: absolute; left: 0; top: 22px; width: 867px; text-align: center; font-size: 19px; font-weight: 700; color: var(--white); text-shadow: 0 2px 4px rgba(0,0,0,.5); }
  .hero-arrow { position: absolute; top: 145px; width: 36px; height: 36px; border-radius: 50%; background: rgba(0,0,0,.45); display: flex; align-items: center; justify-content: center; }
  .hero-arrow.prev { left: 20px; }
  .hero-arrow.next { right: 20px; }

  /* Services */
  .services { position: absolute; left: 95px; top: 440px; width: 677px; height: 232px; background: var(--white); box-shadow: 0 1px 4px rgba(0,0,0,.12); padding: 16px 14px; }
  .section-title { font-size: 13px; font-weight: 800; color: var(--red); text-transform: uppercase; padding-bottom: 6px; border-bottom: 1px solid var(--line); }
  .service-grid { display: flex; gap: 14px; margin-top: 12px; }
  .service { width: 152px; }
  .service-photo { width: 152px; height: 100px; }
  .service h3 { font-size: 10px; font-weight: 800; color: var(--navy); margin: 8px 0 4px; text-transform: uppercase; }
  .service p { font-size: 8.5px; line-height: 1.45; color: var(--muted); }
  .service p span { color: var(--blue); font-weight: 700; }

  /* Welcome + Inquiry */
  .panel-head { display: flex; align-items: center; gap: 8px; height: 26px; background: #e8ebee; padding-left: 6px; font-size: 13px; font-weight: 800; color: var(--navy); text-transform: uppercase; }
  .panel-head i { width: 12px; height: 12px; background: var(--red); display: block; }
  .welcome { position: absolute; left: 95px; top: 700px; width: 330px; }
  .welcome-body { display: flex; gap: 10px; margin-top: 12px; }
  .welcome-photo { width: 132px; height: 96px; flex: none; }
  .welcome p { font-size: 8.5px; line-height: 1.5; color: var(--muted); }
  .welcome .wide { margin-top: 6px; }
  .read-more { display: inline-block; margin-top: 10px; background: var(--blue); color: var(--white); font-size: 9px; font-weight: 700; padding: 5px 10px; border-radius: 2px; }
  .inquiry { position: absolute; left: 470px; top: 700px; width: 302px; }
  .inquiry-form { margin-top: 12px; padding-left: 22px; }
  .field { display: flex; align-items: flex-start; margin-bottom: 9px; font-size: 9px; color: var(--ink); }
  .field label { width: 64px; padding-top: 3px; }
  .field .box { width: 136px; height: 17px; border: 1px solid var(--line); background: var(--white); }
  .field .box.tall { height: 52px; }
  .submit { margin-left: 64px; width: 52px; height: 17px; background: var(--blue); color: var(--white); font-size: 9px; font-weight: 700; display: flex; align-items: center; justify-content: center; border-radius: 2px; }

  /* Footer */
  .site-footer { position: absolute; left: 0; top: 960px; width: 867px; height: 240px; }
  .footer-curve { position: absolute; left: 0; top: 0; }
  .footer-col { position: absolute; top: 62px; color: var(--white); font-size: 9px; }
  .footer-col h4 { font-size: 12px; font-weight: 700; margin-bottom: 12px; }
  .links { left: 105px; }
  .links li { list-style: none; margin-bottom: 6px; display: flex; align-items: center; gap: 6px; }
  .links li::before { content: ""; width: 4px; height: 4px; border-radius: 50%; background: var(--gold); }
  .contact { left: 260px; width: 190px; }
  .contact .row { display: flex; gap: 8px; margin-bottom: 8px; line-height: 1.4; }
  .award-badge { position: absolute; left: 495px; top: 58px; width: 84px; height: 84px; border-radius: 50%; background: radial-gradient(circle, #f7d35a 0%, #d9a418 70%, #a87a0c 100%); }
  .footer-brand { position: absolute; left: 615px; top: 82px; display: flex; align-items: center; gap: 10px; }
  .footer-brand .brand-mark { background: var(--white); }
  .footer-brand .brand-name { color: var(--white); }
  .copyright { position: absolute; left: 0; bottom: 0; width: 867px; height: 22px; background: var(--navy-dark); color: #c9d2de; font-size: 8.5px; display: flex; align-items: center; padding-left: 105px; }
</style>
</head>
<body>
<div class="site">

  <header class="site-header">
    <div class="brand"><span class="brand-mark"></span><span class="brand-name">KVR Service</span></div>
    <div class="topbar">
      <span class="social-dot"></span><span class="social-dot"></span><span class="social-dot"></span><span class="social-dot"></span>
      <span class="email">
        <svg width="11" height="8" viewBox="0 0 11 8"><rect x=".5" y=".5" width="10" height="7" fill="none" stroke="#fff"/><path d="M.5 .5 5.5 4.5 10.5 .5" fill="none" stroke="#fff"/></svg>
        info@kvrservice.com
      </span>
      <span class="phone">
        <svg width="9" height="9" viewBox="0 0 10 10"><path d="M2 0h2l1 3-1.5 1a6 6 0 0 0 2.5 2.5L7 5l3 1v2a2 2 0 0 1-2 2A8 8 0 0 1 0 2a2 2 0 0 1 2-2z" fill="#fff"/></svg>
        (215) 555-0142
      </span>
    </div>
    <nav class="main-nav">
      <a class="active" href="#">HOME</a><a href="#">ABOUT US</a><a href="#">SERVICES</a><a href="#">CONTACT US</a>
    </nav>
    <div class="buy-button">Buy at Brindlemart</div>
  </header>

  <section class="hero" role="img" aria-label="Smiling family relaxing together in a bright living room">
    <h1 class="hero-title">We Are A Residential, Family Owned And Operated Hvac And Plumbing Company</h1>
    <span class="hero-arrow prev"><svg width="12" height="14" viewBox="0 0 12 14"><path d="M9 1 3 7l6 6" fill="none" stroke="#fff" stroke-width="2.5"/></svg></span>
    <span class="hero-arrow next"><svg width="12" height="14" viewBox="0 0 12 14"><path d="M3 1l6 6-6 6" fill="none" stroke="#fff" stroke-width="2.5"/></svg></span>
  </section>

  <section class="services">
    <h2 class="section-title">The Services We Perform</h2>
    <div class="service-grid">
      <article class="service">
        <div class="service-photo" role="img" aria-label="Technician repairing wiring on an air conditioning unit" style="background:linear-gradient(135deg,#3d6f9a,#c7a352)"></div>
        <h3>Repair</h3>
        <p>Fast, honest repairs for furnaces, air conditioners, water heaters and pipes. <span>[more]</span></p>
      </article>
      <article class="service">
        <div class="service-photo" role="img" aria-label="Technician replacing an outdoor cooling unit" style="background:linear-gradient(135deg,#8fa3b3,#5d6a74)"></div>
        <h3>Replacement</h3>
        <p>Upgrade worn out systems with efficient equipment sized right for your home. <span>[more]</span></p>
      </article>
      <article class="service">
        <div class="service-photo" role="img" aria-label="Technician performing maintenance on a condenser" style="background:linear-gradient(135deg,#4b6e86,#b9c3c8)"></div>
        <h3>Maintenance</h3>
        <p>Seasonal tune ups that keep your system safe, clean and running longer. <span>[more]</span></p>
      </article>
      <article class="service">
        <div class="service-photo" role="img" aria-label="Newly installed outdoor HVAC units beside a house" style="background:linear-gradient(135deg,#9eb0b8,#6f7d72)"></div>
        <h3>New Installations</h3>
        <p>Complete installs of heating, cooling and plumbing done neatly on schedule. <span>[more]</span></p>
      </article>
    </div>
  </section>

  <section class="welcome">
    <h2 class="panel-head"><i></i>Welcome to KVR Service</h2>
    <div class="welcome-body">
      <div class="welcome-photo" role="img" aria-label="Technician checking gauges on a heating system" style="background:linear-gradient(135deg,#5a7d99,#d3c8a8)"></div>
      <div>
        <p>Family owned and operated, we bring over twenty years of hands on experience to every home we visit. We started this business to offer fair pricing without cutting corners. Customer service is the only thing that matters to us. We stay small on purpose so every call gets the care it deserves, from the first visit to the last check.</p>
      </div>
    </div>
    <p class="wide">Our owner, one technician and a helper handle every job personally across Bucks, Montgomery and Delaware Counties.</p>
    <span class="read-more">Read More</span>
  </section>

  <section class="inquiry">
    <h2 class="panel-head"><i></i>Quick Inquiry</h2>
    <div class="inquiry-form">
      <div class="field"><label>Name :</label><span class="box"></span></div>
      <div class="field"><label>Company :</label><span class="box"></span></div>
      <div class="field"><label>Subject :</label><span class="box"></span></div>
      <div class="field"><label>Message :</label><span class="box tall"></span></div>
      <div class="submit">Submit</div>
    </div>
  </section>

  <footer class="site-footer">
    <svg class="footer-curve" width="867" height="240" viewBox="0 0 867 240">
      <path d="M0 30 Q433 -20 867 30 V240 H0 Z" fill="#1b3764"/>
      <path d="M0 30 Q433 -20 867 30" fill="none" stroke="#0255a3" stroke-width="4"/>
    </svg>
    <div class="footer-col links">
      <h4>Quick Links</h4>
      <ul><li>Home</li><li>About Us</li><li>Services</li><li>Contact Us</li></ul>
    </div>
    <div class="footer-col contact">
      <h4>Contact Information</h4>
      <div class="row">
        <svg width="9" height="12" viewBox="0 0 9 12"><path d="M4.5 0A4.5 4.5 0 0 0 0 4.5C0 8 4.5 12 4.5 12S9 8 9 4.5A4.5 4.5 0 0 0 4.5 0zm0 6.3a1.8 1.8 0 1 1 0-3.6 1.8 1.8 0 0 1 0 3.6z" fill="#fff"/></svg>
        <span>KVR Service<br>1482 Orchard Lane, Suite 4,<br>Doylestown, PA 18901</span>
      </div>
      <div class="row">
        <svg width="9" height="9" viewBox="0 0 10 10"><path d="M2 0h2l1 3-1.5 1a6 6 0 0 0 2.5 2.5L7 5l3 1v2a2 2 0 0 1-2 2A8 8 0 0 1 0 2a2 2 0 0 1 2-2z" fill="#fff"/></svg>
        <span>(215) 555-0142</span>
      </div>
      <div class="row">
        <svg width="10" height="8" viewBox="0 0 11 8"><rect x=".5" y=".5" width="10" height="7" fill="none" stroke="#fff"/><path d="M.5 .5 5.5 4.5 10.5 .5" fill="none" stroke="#fff"/></svg>
        <span>info@kvrservice.com</span>
      </div>
    </div>
    <div class="award-badge" role="img" aria-label="Harlow's guide top trade award badge"></div>
    <div class="footer-brand"><span class="brand-mark"></span><span class="brand-name">KVR Service</span></div>
    <div class="copyright">Copyright © 2015 KVR Service &nbsp;|&nbsp; All Rights Reserved</div>
  </footer>

</div>
</body>
</html>
```